WebSite

Hi,

I need a (responsive?) website for a company that has 3 core businesses:

Hosting
Web design (also logo design)
and ICT systems management

The hosting part has a whois that can be searched, and from there a domain can be registered or moved if it is taken and the move code is known.
Also a pricelist for the 4 different types of packages + add-ons.

The web design part has got to have a small portfolio section.

The ICT management section is just an ordinary page with some info on the work the company does.

And off course a contact page...

http://sh1.vq-serverhuis.nl/cgi-sys/defaultwebpage.cgi

It is a Dutch company, the logo is provided.

I like clean designs, not to busy or to dark, just good look and feel and modern!

I like those single page (with pages that flout into each other etc.) designs (like: http://www.gullweave.com/tovu) but that kind of sites needs to be coded also, that would be part of the job than!

This is my first time here so I do not know if more information is needed or what happens next :)
Updates

http://lomberquay.com/#!portfolio-dmesk to give another example of what I like, a site like that is great! 

Hello,

I recieved some designs already but I was hoping for some more creativity, I do not want a design I can buy at Layoutgrotto, I really am in need for something that goes with my logo and looks unique (see last link from brief).

Industry/Entity Type

It Company

Logo Text

VQ Services

```html
<!DOCTYPE html>
<html lang="nl">
<head>
<meta charset="utf-8">
<title>VQ Services – Hosting, Web Design &amp; ICT Systems Management</title>
<link rel="stylesheet" href="https://fonts.googleapis.com/css2?family=Open+Sans:wght@400;600;700&family=Oswald:wght@400;500;700&display=swap">
<style>
  :root {
    --navy: #0b3a6e;
    --blue: #11508f;
    --blue-bright: #1d7fd0;
    --blue-light: #2a95dd;
    --green: #6cb41c;
    --green-dark: #3f6d10;
    --purple: #6b3c9e;
    --coral: #f2736f;
    --teal: #3bc8b6;
    --orange: #f07a1a;
    --ink: #2b2b2b;
    --muted: #666;
    --line: #d6d6d6;
    --panel: #f3f3f3;
    --table-head: #2b2b2b;
    --white: #ffffff;
  }
  * { box-sizing: border-box; margin: 0; padding: 0; }
  html, body { width: 1200px; height: 3270px; overflow: hidden; }
  body {
    position: relative;
    font-family: "Open Sans", Arial, sans-serif;
    color: var(--ink);
    background: var(--white);
  }
  .heading {
    font-family: "Oswald", "Arial Narrow", sans-serif;
    font-weight: 700;
    color: var(--navy);
    text-transform: uppercase;
  }

  /* Header */
  .site-header {
    position: absolute; top: 0; left: 0; width: 1200px; height: 108px;
    background: var(--white);
    border-bottom: 1px solid #e3e3e3;
  }
  .brand {
    position: absolute; left: 147px; top: 28px;
    display: flex; align-items: center; gap: 12px;
  }
  .brand-dot { width: 40px; height: 40px; border-radius: 50%; background: var(--navy); }
  .brand-name { font-weight: 700; font-size: 30px; color: var(--navy); letter-spacing: .5px; }
  .main-nav {
    position: absolute; left: 640px; top: 38px;
    display: flex; gap: 14px; align-items: center;
  }
  .main-nav a {
    font-family: "Oswald", sans-serif; font-weight: 500; font-size: 16px;
    color: var(--navy); text-decoration: none; text-transform: uppercase;
    padding: 6px 12px; border-radius: 15px;
  }
  .main-nav a.is-active { background: var(--navy); color: var(--white); font-size: 14px; }

  /* Hero / domain search */
  .hero {
    position: absolute; top: 108px; left: 0; width: 1200px; height: 546px;
    background: linear-gradient(90deg, #eef1f4 0%, #f6f7f9 40%, #dfe4ea 100%);
    overflow: hidden;
  }
  .hero-office {
    position: absolute; left: 0; top: 0; width: 1200px; height: 546px;
    background: radial-gradient(ellipse at 20% 40%, rgba(255,255,255,.9), rgba(220,226,233,.6) 70%);
  }
  .hero-person {
    position: absolute; left: 640px; top: 0; width: 420px; height: 546px;
    background: linear-gradient(180deg, #d9c9bd 0%, #c6b1a3 35%, #f0eeec 60%, #e6e2df 100%);
  }
  .hero-title { position: absolute; left: 140px; top: 120px; width: 470px; text-align: center; }
  .hero-title .kicker { font-size: 32px; line-height: 1; color: var(--navy); }
  .hero-title .domain { font-size: 64px; line-height: 1.1; margin-top: 6px; }
  .price-badge {
    position: absolute; left: 642px; top: 80px; width: 96px; height: 96px;
    border-radius: 50%; background: var(--purple); color: var(--white);
    text-align: center; font-family: "Oswald", sans-serif; font-weight: 700;
  }
  .price-badge .tld { display: block; font-size: 15px; margin-top: 18px; line-height: 1; }
  .price-badge .amount { display: block; font-size: 34px; line-height: 1.1; }
  .price-badge .amount sup { font-size: 13px; }
  .domain-search {
    position: absolute; left: 140px; top: 272px; width: 530px; height: 60px;
    display: flex; border: 3px solid #26331b; background: var(--white);
  }
  .domain-input {
    flex: 1; display: flex; align-items: center; padding-left: 16px;
    font-size: 22px; color: var(--ink);
  }
  .domain-ext {
    width: 110px; margin: 8px 10px 8px 0; border: 1px solid var(--line);
    display: flex; align-items: center; justify-content: space-between;
    padding: 0 10px; font-size: 18px;
  }
  .domain-go {
    width: 100px; background: var(--green); border-left: 3px solid #26331b;
    color: #1f2b12; font-family: "Oswald", sans-serif; font-weight: 700;
    font-size: 30px; display: flex; align-items: center; justify-content: center;
  }
  .hero-note {
    position: absolute; left: 140px; top: 350px; width: 530px;
    font-size: 14px; line-height: 1.55; text-align: center; color: var(--ink);
  }

  /* Hosting plans */
  .hosting {
    position: absolute; top: 654px; left: 0; width: 1200px; height: 686px;
    background:
      radial-gradient(ellipse 700px 260px at 50% 0%, rgba(80,170,240,.55), transparent 70%),
      linear-gradient(180deg, #0a2f5c 0%, #0d4a8c 45%, #1466b6 100%);
  }
  .hosting-title {
    position: absolute; left: 140px; top: 32px;
    font-family: "Oswald", sans-serif; font-weight: 700; font-size: 24px;
    color: var(--white); text-transform: uppercase;
  }
  .plan-table { position: absolute; left: 140px; top: 124px; display: flex; align-items: flex-start; }
  .plan-col { background: linear-gradient(90deg, #e4e4e4, #f7f7f7); }
  .plan-col--label { width: 203px; }
  .plan-col--small { width: 157px; }
  .plan-col--featured {
    width: 197px; margin-top: -20px; background: var(--white);
    box-shadow: 0 8px 24px rgba(0,0,0,.45); position: relative; z-index: 1;
    padding-bottom: 20px;
  }
  .plan-col--large { width: 170px; }
  .plan-col--xl { width: 196px; }
  .plan-head {
    height: 40px; background: var(--table-head); color: var(--white);
    font-size: 18px; display: flex; align-items: center; justify-content: center;
  }
  .plan-col--label .plan-head { justify-content: flex-start; padding-left: 14px; }
  .plan-col--featured .plan-head { height: 60px; background: var(--green); color: #1f2b12; padding-top: 20px; }
  .plan-row {
    height: 24px; border-bottom: 1px solid var(--line);
    font-size: 11px; color: #555; display: flex; align-items: center; padding-left: 14px;
    white-space: nowrap; overflow: hidden;
  }
  .plan-gap { height: 44px; }
  .plan-price {
    height: 40px; border-top: 1px solid var(--line); font-size: 12px;
    display: flex; align-items: center; padding-left: 14px; color: #444; line-height: 1.25;
  }

  /* Web design */
  .web-design { position: absolute; top: 1340px; left: 0; width: 1200px; height: 240px; background: var(--white); }
  .section-title { position: absolute; left: 0; width: 1200px; text-align: center; font-size: 42px; }
  .section-title::after {
    content: ""; display: block; width: 120px; height: 2px; background: var(--navy);
    margin: 8px auto 0;
  }
  .web-design .section-title { top: 52px; }
  .filters {
    position: absolute; top: 150px; left: 0; width: 1200px;
    display: flex; justify-content: center; gap: 6px;
  }
  .filters span {
    border: 1px solid var(--line); font-size: 12px; font-weight: 600;
    padding: 7px 14px; color: #555; text-transform: uppercase;
  }
  .filters span.is-active { background: var(--green); color: var(--white); border-color: var(--green); }

  .portfolio {
    position: absolute; top: 1580px; left: 0; width: 1200px; height: 600px;
    display: grid; grid-template-columns: repeat(6, 200px); grid-auto-rows: 200px;
  }
  .tile {
    position: relative; display: flex; flex-direction: column;
    align-items: center; justify-content: center; color: var(--white);
    font-family: "Oswald", sans-serif; text-transform: uppercase; text-align: center;
  }
  .tile-icon { width: 34px; height: 34px; margin-bottom: 10px; }
  .tile-name { font-size: 24px; font-weight: 400; line-height: 1; }
  .tile-sub { font-size: 11px; letter-spacing: 1px; margin-top: 6px; font-family: "Open Sans", sans-serif; }
  .tile--coral { background: var(--coral); }
  .tile--teal { background: var(--teal); }
  .tile--letters { background: linear-gradient(135deg, #f2e6cf, #d7c5a4); }
  .tile--badge-dark { background: linear-gradient(180deg, #f4f4f4, #e2e2e2); }
  .tile--industrial { background: linear-gradient(180deg, #444, #2c2c2c); }
  .tile--flowers { background: radial-gradient(circle at 50% 45%, #f2d21a, #9c8a3b 70%, #6f6e58); }
  .tile--grass { background: linear-gradient(160deg, #8fcf3a, #3f8a1a); }
  .tile--wood { background: linear-gradient(180deg, #6a3d20, #3e2211); }
  .tile--dark-logo { background: linear-gradient(180deg, #2b2b2b, #141414); }
  .tile--curves { background: linear-gradient(135deg, #f7c21a, #f07a18 50%, #d8431b); }
  .tile--grass-card { background: linear-gradient(160deg, #4d8a22, #2f5c17); }
  .tile--stationery { background: linear-gradient(135deg, #f2f2f2, #cfcfcf); }

  /* ICT */
  .ict { position: absolute; top: 2180px; left: 0; width: 1200px; height: 550px; background: var(--panel); }
  .ict .section-title { top: 48px; }
  .ict-intro {
    position: absolute; top: 148px; left: 150px; width: 900px;
    font-size: 14px; line-height: 1.6; text-align: center; color: #444;
  }
  .service { position: absolute; top: 250px; width: 290px; }
  .service--one { left: 206px; }
  .service--two { left: 533px; }
  .service--three { left: 850px; }
  .service-icon { width: 52px; height: 52px; margin-bottom: 14px; }
  .service-title { font-family: "Oswald", sans-serif; font-weight: 500; font-size: 22px; text-transform: uppercase; line-height: 1.2; }
  .service--one .service-title { color: var(--orange); }
  .service--two .service-title { color: var(--blue-light); }
  .service--three .service-title { color: var(--green); }
  .service-text { font-size: 13px; line-height: 1.55; color: #444; margin-top: 6px; }
  .service-more { display: block; font-size: 13px; font-weight: 600; color: var(--ink); margin: 8px 0 0 40px; }

  /* Contact */
  .contact {
    position: absolute; top: 2730px; left: 0; width: 1200px; height: 490px;
    background: linear-gradient(180deg, #0c2748 0%, #0e3a6c 50%, #0a2a50 100%);
  }
  .contact-skyline {
    position: absolute; inset: 0;
    background: linear-gradient(180deg, rgba(40,90,150,.35), rgba(10,30,60,.2));
  }
  .contact .section-title { top: 54px; color: var(--white); }
  .contact .section-title::after { background: var(--white); }
  .contact-intro {
    position: absolute; left: 140px; top: 160px; width: 500px;
    color: var(--white); font-size: 14px; line-height: 1.6;
  }
  .contact-details { position: absolute; left: 140px; top: 268px; list-style: none; color: var(--white); font-size: 12px; }
  .contact-details li { display: flex; align-items: center; gap: 12px; height: 26px; }
  .contact-details svg { width: 16px; height: 16px; }
  .contact-form { position: absolute; left: 697px; top: 180px; width: 366px; }
  .form-row { display: flex; gap: 12px; }
  .field {
    flex: 1; height: 34px; border-bottom: 1px solid rgba(255,255,255,.5);
    color: #c9d6e6; font-size: 12px; padding: 8px 4px;
  }
  .field--message { height: 112px; margin-top: 14px; border: 1px solid rgba(255,255,255,.25); border-bottom-color: rgba(255,255,255,.5); }
  .send-button {
    margin-top: 28px; height: 40px; background: var(--blue-bright); color: var(--white);
    font-size: 14px; font-weight: 600; text-transform: uppercase; letter-spacing: .5px;
    display: flex; align-items: center; justify-content: center;
  }

  .site-footer {
    position: absolute; top: 3220px; left: 0; width: 1200px; height: 50px;
    display: flex; align-items: center; justify-content: center;
    font-size: 12px; color: #444; background: var(--white);
  }
</style>
</head>
<body>

<header class="site-header">
  <div class="brand">
    <span class="brand-dot"></span>
    <span class="brand-name">VQ Services</span>
  </div>
  <nav class="main-nav">
    <a class="is-active" href="#hosting">Hosting</a>
    <a href="#webdesign">Web Design</a>
    <a href="#ict">ICT Systems Management</a>
  </nav>
</header>

<section class="hero" id="hosting">
  <div class="hero-office" role="img" aria-label="Vervaagde kantooromgeving op de achtergrond"></div>
  <div class="hero-person" role="img" aria-label="Glimlachende medewerker van de klantenservice"></div>
  <div class="hero-title">
    <div class="heading kicker">Typ hier de</div>
    <div class="heading domain">Domeinnaam</div>
  </div>
  <div class="price-badge">
    <span class="tld">.com</span>
    <span class="amount">1,<sup>95</sup></span>
  </div>
  <div class="domain-search">
    <div class="domain-input">www.</div>
    <div class="domain-ext">.com
      <svg width="10" height="8" viewBox="0 0 10 8"><path d="M0 0h10L5 8z" fill="#333"/></svg>
    </div>
    <div class="domain-go">GO</div>
  </div>
  <p class="hero-note">Gebruik het zoekveld hierboven om de beschikbaarheid van een domeinnaam te controleren. Probeer hierbij geen "http://www." of extensies (.nl, .com etc) te gebruiken.</p>
</section>

<section class="hosting">
  <h2 class="hosting-title">Domeinhosting (.nl .com .be .de .net)</h2>
  <div class="plan-table">
    <div class="plan-col plan-col--label">
      <div class="plan-head">Pakket:</div>
      <div class="plan-row">Ruimte</div>
      <div class="plan-row">Pop3</div>
      <div class="plan-row">Mail forward</div>
      <div class="plan-row">Databases</div>
      <div class="plan-row">Subdomeinen</div>
      <div class="plan-row">Dataverkeer</div>
      <div class="plan-row">Gratis domein(en)</div>
      <div class="plan-row">Parked domein(en)</div>
      <div class="plan-row">Site-editor extensies</div>
      <div class="plan-row">PHP ondersteuning</div>
      <div class="plan-row">Beheerpaneel toegang</div>
      <div class="plan-gap"></div>
      <div class="plan-price">Prijzen (per jaar)</div>
      <div class="plan-price">Prijzen (zonder domeinnaam)<br>(per jaar)</div>
    </div>
    <div class="plan-col plan-col--small">
      <div class="plan-head">VQ Small</div>
      <div class="plan-row">50MB</div><div class="plan-row">5</div><div class="plan-row">5</div>
      <div class="plan-row">1</div><div class="plan-row">Ja</div><div class="plan-row">1.0GB</div>
      <div class="plan-row">1</div><div class="plan-row">Ja</div><div class="plan-row">Ja</div>
      <div class="plan-row">Ja</div><div class="plan-row">Ja</div>
      <div class="plan-gap"></div>
      <div class="plan-price">€ 30</div><div class="plan-price">€ 37,50</div>
    </div>
    <div class="plan-col plan-col--featured">
      <div class="plan-head">VQ Medium</div>
      <div class="plan-row">250MB</div><div class="plan-row">50</div><div class="plan-row">50</div>
      <div class="plan-row">2</div><div class="plan-row">Ja</div><div class="plan-row">4GB</div>
      <div class="plan-row">1</div><div class="plan-row">Ja</div><div class="plan-row">Ja</div>
      <div class="plan-row">Ja</div><div class="plan-row">Ja</div>
      <div class="plan-gap"></div>
      <div class="plan-price">€ 120</div><div class="plan-price">€ 112,50</div>
    </div>
    <div class="plan-col plan-col--large">
      <div class="plan-head">VQ Large</div>
      <div class="plan-row">500MB</div><div class="plan-row">100</div><div class="plan-row">100</div>
      <div class="plan-row">5</div><div class="plan-row">Ja</div><div class="plan-row">8GB</div>
      <div class="plan-row">2</div><div class="plan-row">Ja</div><div class="plan-row">Ja</div>
      <div class="plan-row">Ja</div><div class="plan-row">Ja</div>
      <div class="plan-gap"></div>
      <div class="plan-price">€ 250</div><div class="plan-price">€ 225</div>
    </div>
    <div class="plan-col plan-col--xl">
      <div class="plan-head">VQ Xtra Large</div>
      <div class="plan-row">2000MB</div><div class="plan-row">Onbeperkt</div><div class="plan-row">Onbeperkt</div>
      <div class="plan-row">15</div><div class="plan-row">Ja</div><div class="plan-row">20GB</div>
      <div class="plan-row">3</div><div class="plan-row">Ja</div><div class="plan-row">Ja</div>
      <div class="plan-row">Ja</div><div class="plan-row">Ja</div>
      <div class="plan-gap"></div>
      <div class="plan-price">€ 500</div><div class="plan-price">€ 475</div>
    </div>
  </div>
</section>

<section class="web-design" id="webdesign">
  <h2 class="heading section-title">Web Design</h2>
  <div class="filters">
    <span>All</span><span>Websites</span><span class="is-active">Logos</span><span>Video</span><span>Graphic</span>
  </div>
</section>

<div class="portfolio">
  <div class="tile tile--letters" role="img" aria-label="Typografisch ontwerp met grote letters"></div>
  <div class="tile tile--coral">
    <svg class="tile-icon" viewBox="0 0 34 34" fill="none" stroke="#fff" stroke-width="2"><rect x="3" y="6" width="28" height="22"/><path d="M3 24l9-9 7 7 5-5 7 7"/></svg>
    <span class="tile-name">Gallery</span><span class="tile-sub">Choose your style</span>
  </div>
  <div class="tile tile--badge-dark" role="img" aria-label="Logo-ontwerp: embleem NOV"></div>
  <div class="tile tile--industrial" role="img" aria-label="Logo-ontwerp: Tarven Works Co."></div>
  <div class="tile tile--coral">
    <svg class="tile-icon" viewBox="0 0 34 34" fill="none" stroke="#fff" stroke-width="2"><rect x="3" y="6" width="28" height="22"/><path d="M3 24l9-9 7 7 5-5 7 7"/></svg>
    <span class="tile-name">Gallery</span><span class="tile-sub">Choose your style</span>
  </div>
  <div class="tile tile--flowers" role="img" aria-label="Foto van gele bloemen"></div>

  <div class="tile tile--coral">
    <svg class="tile-icon" viewBox="0 0 34 34" fill="none" stroke="#fff" stroke-width="2"><path d="M6 28L26 8l2 2L8 30H6z"/></svg>
    <span class="tile-name">Our Blog</span><span class="tile-sub">2015 - 2016</span>
  </div>
  <div class="tile tile--grass" role="img" aria-label="Foto van gras"></div>
  <div class="tile tile--teal">
    <svg class="tile-icon" viewBox="0 0 34 34" fill="none" stroke="#fff" stroke-width="2"><rect x="6" y="12" width="22" height="18"/><path d="M12 12V8a5 5 0 0 1 10 0v4"/></svg>
    <span class="tile-name">Our Store</span><span class="tile-sub">2016</span>
  </div>
  <div class="tile tile--coral">
    <svg class="tile-icon" viewBox="0 0 34 34" fill="none" stroke="#fff" stroke-width="2"><path d="M6 28L26 8l2 2L8 30H6z"/></svg>
    <span class="tile-name">Our Blog</span><span class="tile-sub">2015 - 2016</span>
  </div>
  <div class="tile tile--wood" role="img" aria-label="Logo-ontwerp Harlow op houten achtergrond"></div>
  <div class="tile tile--coral">
    <svg class="tile-icon" viewBox="0 0 34 34" fill="none" stroke="#fff" stroke-width="2"><path d="M6 28L26 8l2 2L8 30H6z"/></svg>
    <span class="tile-name">Our Blog</span><span class="tile-sub">2015 - 2016</span>
  </div>

  <div class="tile tile--teal">
    <svg class="tile-icon" viewBox="0 0 34 34" fill="none" stroke="#fff" stroke-width="2"><rect x="6" y="12" width="22" height="18"/><path d="M12 12V8a5 5 0 0 1 10 0v4"/></svg>
    <span class="tile-name">Our Store</span><span class="tile-sub">2016</span>
  </div>
  <div class="tile tile--dark-logo" role="img" aria-label="Logo-ontwerp Little Kite op donkere achtergrond"></div>
  <div class="tile tile--coral">
    <svg class="tile-icon" viewBox="0 0 34 34" fill="none" stroke="#fff" stroke-width="2"><rect x="3" y="6" width="28" height="22"/><path d="M3 24l9-9 7 7 5-5 7 7"/></svg>
    <span class="tile-name">Gallery</span><span class="tile-sub">Choose your style</span>
  </div>
  <div class="tile tile--curves" role="img" aria-label="Abstracte oranje golven"></div>
  <div class="tile tile--grass-card" role="img" aria-label="Visitekaartje op gras"></div>
  <div class="tile tile--stationery" role="img" aria-label="Huisstijl drukwerk op lichte ondergrond"></div>
</div>

<section class="ict" id="ict">
  <h2 class="heading section-title">ICT Systems Management</h2>
  <p class="ict-intro">Lorem Ipsum is simply dummy text of the printing and typesetting industry. Lorem Ipsum has been the industry's standard dummy text ever since the 1500s, when an unknown printer took a galley of type and scrambled it to make a type specimen book.</p>

  <div class="service service--one">
    <svg class="service-icon" viewBox="0 0 52 52" fill="none" stroke="#f07a1a" stroke-width="3"><path d="M4 12h18a4 4 0 0 1 4 4v28a4 4 0 0 0-4-4H4z"/><path d="M48 12H30a4 4 0 0 0-4 4v28a4 4 0 0 1 4-4h18z"/></svg>
    <div class="service-title">Lorem Ipsum Is</div>
    <p class="service-text">Lorem Ipsum is simply dummy text of the printing and typesetting industry. Lorem Ipsum has.</p>
    <span class="service-more">Read More...</span>
  </div>
  <div class="service service--two">
    <svg class="service-icon" viewBox="0 0 52 52" fill="none" stroke="#2a95dd" stroke-width="3"><circle cx="26" cy="26" r="9"/><path d="M26 4v8M26 40v8M4 26h8M40 26h8M10 10l6 6M36 36l6 6M10 42l6-6M36 16l6-6"/></svg>
    <div class="service-title">Lorem Ipsum Is</div>
    <p class="service-text">Lorem Ipsum is simply dummy text of the printing and typesetting industry. Lorem Ipsum has.</p>
    <span class="service-more">Read More...</span>
  </div>
  <div class="service service--three">
    <svg class="service-icon" viewBox="0 0 52 52" fill="none" stroke="#6cb41c" stroke-width="3"><rect x="4" y="8" width="44" height="28"/><path d="M18 46h16M26 36v10"/><path d="M18 22l6 6 10-12"/></svg>
    <div class="service-title">Lorem Ipsum Is</div>
    <p class="service-text">Lorem Ipsum is simply dummy text of the printing and typesetting industry. Lorem Ipsum has.</p>
    <span class="service-more">Read More...</span>
  </div>
</section>

<section class="contact">
  <div class="contact-skyline" role="img" aria-label="Skyline met kantoorgebouwen in blauwe tinten"></div>
  <h2 class="heading section-title">Contact Us</h2>
  <p class="contact-intro">Lorem ipsum dolor sit amet, consectetur adipiscing elit. Duis auctor est eget lobortis dictum. Mauris dolor felis, rutrum quis elit ut, adipiscing accumsan nulla. Suspendisse neque velit, tincidunt a elit nec, blandit sit amet dolor.</p>
  <ul class="contact-details">
    <li><svg viewBox="0 0 16 16" fill="#fff"><path d="M8 0a5 5 0 0 0-5 5c0 4 5 11 5 11s5-7 5-11a5 5 0 0 0-5-5zm0 7a2 2 0 1 1 0-4 2 2 0 0 1 0 4z"/></svg>1234 Street Name, City Name, United States</li>
    <li><svg viewBox="0 0 16 16" fill="#fff"><path d="M3 1l3 3-2 2c1 2 3 4 5 5l2-2 3 3-2 3C6 15 1 10 1 3z"/></svg>(123) 567-907</li>
    <li><svg viewBox="0 0 16 16" fill="none" stroke="#fff" stroke-width="1.5"><rect x="1" y="3" width="14" height="10"/><path d="M1 3l7 6 7-6"/></svg>contact@vq-services.nl</li>
  </ul>
  <div class="contact-form">
    <div class="form-row">
      <div class="field">Your Name</div>
      <div class="field">Your email address</div>
    </div>
    <div class="field field--message">Message</div>
    <div class="send-button">Send Message</div>
  </div>
</section>

<footer class="site-footer">© Copyright 2014 - vq-services.nl. All rights reserved.</footer>

</body>
</html>
```